Harbor LVT, sample binder

I'm looking for sample book cover and spine design using super deep, rich saturated colors starting with Royal Blue and Gold lettering. I need the front cover to Say:ELITELVTand in tiny letters below "by Vantoria".Around the HARBOR and LVT which should be slightly smaller, I would like something like 5 Stars or 5 Diamonds and maybe curved Fig type leaves? On the Spine the word HARBOR must be vertical with at the bottom smaller LVT and below LVT the number 9 at the bottom.A deep Blue is my first choice but please post a deep Maroon to. i'm up for Rich and Elegant ideas, so please be creative!!Keep in mind this is a Flooring company in your design ideas.Thank you,MikeFYI, LVT stands for Luxury Vinyl Tile

```html
<!DOCTYPE html>
<html lang="en">
<head>
<meta charset="utf-8">
<title>Harbor LVT — Sample Binder Cover</title>
<link rel="stylesheet" href="https://fonts.googleapis.com/css2?family=Cinzel:wght@400;500&display=swap">
<style>
  :root {
    --backdrop: #030736;
    --royal: #1a2ea3;
    --royal-deep: #101f86;
    --navy-panel: #141a4a;
    --night: #0d1030;
    --gold: #c9975a;
    --gold-light: #f0cf8e;
    --ivory: #e8e6f2;
  }
  html, body {
    margin: 0;
    width: 1200px;
    height: 900px;
    overflow: hidden;
    background: var(--backdrop);
  }
  .stage {
    width: 1200px;
    height: 900px;
    display: flex;
    align-items: center;
    justify-content: center;
  }
  .cover {
    width: 540px;
    height: 762px;
    display: block;
  }
  .cover-title {
    font-family: "Cinzel", serif;
    font-size: 42px;
    font-weight: 400;
  }
  .cover-subtitle {
    font-family: "Cinzel", serif;
    font-size: 26px;
    letter-spacing: 3px;
  }
  .cover-byline {
    font-family: "Cinzel", serif;
    font-size: 18px;
    fill: var(--ivory);
    letter-spacing: 2px;
  }
  .cover-volume {
    font-family: "Cinzel", serif;
    font-size: 34px;
  }
</style>
</head>
<body>
<main class="stage">
  <svg class="cover" viewBox="0 0 540 762" xmlns="http://www.w3.org/2000/svg" aria-labelledby="cover-heading">
    <title id="cover-heading">Harbor LVT by Vantoria, volume 9</title>
    <defs>
      <linearGradient id="gold-foil" x1="0" y1="0" x2="1" y2="1">
        <stop offset="0" stop-color="var(--gold-light)"/>
        <stop offset="0.5" stop-color="var(--gold)"/>
        <stop offset="1" stop-color="#a8773f"/>
      </linearGradient>
      <linearGradient id="cloth" x1="0" y1="0" x2="0" y2="1">
        <stop offset="0" stop-color="var(--royal)"/>
        <stop offset="1" stop-color="var(--royal-deep)"/>
      </linearGradient>
    </defs>

    <!-- cloth -->
    <rect class="cover-base" width="540" height="762" fill="url(#cloth)"/>
    <rect class="cover-hinge" x="0" y="0" width="24" height="762" fill="#0b1870" opacity="0.6"/>

    <!-- gold inset rule -->
    <rect class="cover-rule" x="46" y="34" width="470" height="694" fill="none"
          stroke="url(#gold-foil)" stroke-width="1.5"/>

    <!-- five gold diamonds -->
    <g class="diamond-row" fill="url(#gold-foil)">
      <polygon points="211,96 219,104 211,112 203,104"/>
      <polygon points="246,96 254,104 246,112 238,104"/>
      <polygon points="281,94 291,104 281,114 271,104"/>
      <polygon points="316,96 324,104 316,112 308,104"/>
      <polygon points="351,96 359,104 351,112 343,104"/>
    </g>

    <!-- title panel -->
    <rect class="title-panel" x="181" y="136" width="200" height="440"
          fill="var(--navy-panel)" stroke="url(#gold-foil)" stroke-width="4"/>

    <!-- stacked title -->
    <text class="cover-title" fill="url(#gold-foil)" text-anchor="middle">
      <tspan x="281" y="200">H</tspan>
      <tspan x="281" y="254">A</tspan>
      <tspan x="281" y="308">R</tspan>
      <tspan x="281" y="362">B</tspan>
      <tspan x="281" y="416">O</tspan>
      <tspan x="281" y="470">R</tspan>
    </text>
    <text class="cover-subtitle" x="281" y="535" fill="url(#gold-foil)" text-anchor="middle">LVT</text>

    <!-- footer band -->
    <rect class="cover-foot" x="24" y="612" width="516" height="150" fill="var(--night)" opacity="0.85"/>
    <line x1="46" y1="612" x2="516" y2="612" stroke="url(#gold-foil)" stroke-width="1.5"/>

    <!-- byline and volume -->
    <text class="cover-byline" x="281" y="652" text-anchor="middle">BY VANTORIA</text>
    <text class="cover-volume" x="281" y="706" fill="url(#gold-foil)" text-anchor="middle">9</text>
  </svg>
</main>
</body>
</html>
```